Book Cover Design Project

We need a book cover for a eBook on internet banking.

This eBook is meant to be an easy to read, practical book to help people understand what internet banking is, the pros and cons and cover the pure 'internet only' banks that have no branches. The intention is to help people to make informed decisions about whether to use internet banking, how to use it safely and explain in detail what 'internet only' banks are and whether they are right for them.

The cover should not look technical so that non-technical people are not scared off by the look. I have uploaded a book cover design that has the style that I am trying to portray, I have also uploaded a front cover that I created but do not think is suitable.

The cover wording layout could be something like
"Internet Banking"
"A practical guide to answer all your questions" or "The ultimate guide to internet banking" or "The Who's What's and How's of Internet Banking"
Authors name : Clive Mortlock

Industry/Entity Type

Internet

```html
<!DOCTYPE html>
<html lang="en">
<head>
<meta charset="utf-8">
<title>The Ultimate Guide to Internet Banking — Clive Mortlock</title>
<link rel="stylesheet" href="https://fonts.googleapis.com/css2?family=Ubuntu:wght@400&family=Barlow+Condensed:wght@300&display=swap">
<style>
  :root {
    --navy-deep: #0d2360;
    --navy-shadow: #0a1d4f;
    --blue-mid: #1f5a9c;
    --teal-glow: #3f97bd;
    --blue-bright: #2a63b4;
    --haze: #8fb4d8;
    --band: #dfe8f1;
    --band-edge: #c9d9e8;
    --ink-light: #ffffff;
  }
  * { margin: 0; padding: 0; box-sizing: border-box; }
  html, body {
    width: 900px;
    height: 1200px;
    overflow: hidden;
    background: var(--band);
  }
  .cover {
    position: relative;
    width: 900px;
    height: 1200px;
    overflow: hidden;
  }
  .cover-photo {
    position: absolute;
    left: 0; top: 0;
    width: 900px;
    height: 1107px;
    background:
      radial-gradient(ellipse 300px 420px at 640px 520px, rgba(10,29,79,0.75), transparent 70%),
      radial-gradient(ellipse 380px 300px at 330px 560px, rgba(63,151,189,0.7), transparent 70%),
      radial-gradient(ellipse 300px 260px at 180px 850px, rgba(143,180,216,0.45), transparent 75%),
      radial-gradient(ellipse 560px 220px at 450px 1080px, rgba(170,200,230,0.7), transparent 75%),
      linear-gradient(90deg, rgba(13,35,96,0.55) 0%, transparent 30%, transparent 60%, rgba(10,29,79,0.85) 100%),
      linear-gradient(180deg, var(--navy-deep) 0%, var(--blue-bright) 28%, var(--blue-mid) 55%, var(--teal-glow) 82%, var(--haze) 100%);
  }
  .light-streaks {
    position: absolute;
    left: 0; top: 0;
    width: 900px;
    height: 1107px;
  }
  .base-band {
    position: absolute;
    left: 0; top: 1107px;
    width: 900px;
    height: 93px;
    background: linear-gradient(180deg, var(--band-edge) 0%, var(--band) 25%, var(--band) 100%);
  }
  .author {
    position: absolute;
    top: 90px;
    left: 0;
    width: 900px;
    text-align: center;
    font-family: "Ubuntu", sans-serif;
    font-weight: 400;
    font-size: 70px;
    letter-spacing: 3px;
    color: var(--ink-light);
  }
  .title {
    position: absolute;
    top: 722px;
    left: 0;
    width: 900px;
    text-align: center;
    font-family: "Barlow Condensed", sans-serif;
    font-weight: 300;
    color: var(--ink-light);
    text-transform: uppercase;
    text-shadow: 0 0 18px rgba(13,35,96,0.4);
  }
  .title-line {
    display: block;
    font-size: 112px;
    line-height: 117px;
  }
  .title-line--lead { font-size: 100px; }
</style>
</head>
<body>
  <main class="cover">
    <div class="cover-photo" role="img" aria-label="Blue-toned photo of a hand typing on a computer keyboard"></div>
    <svg class="light-streaks" viewBox="0 0 900 1107" aria-hidden="true">
      <g fill="#bfe0f5">
        <rect x="60" y="0" width="6" height="1107" opacity="0.10"/>
        <rect x="118" y="0" width="14" height="1107" opacity="0.08"/>
        <rect x="190" y="0" width="3" height="1107" opacity="0.14"/>
        <rect x="248" y="0" width="22" height="1107" opacity="0.07"/>
        <rect x="312" y="0" width="4" height="1107" opacity="0.13"/>
        <rect x="365" y="0" width="10" height="1107" opacity="0.09"/>
        <rect x="430" y="0" width="3" height="1107" opacity="0.15"/>
        <rect x="488" y="0" width="18" height="1107" opacity="0.07"/>
        <rect x="560" y="0" width="4" height="1107" opacity="0.12"/>
        <rect x="618" y="0" width="8" height="1107" opacity="0.09"/>
        <rect x="680" y="0" width="3" height="1107" opacity="0.14"/>
        <rect x="735" y="0" width="16" height="1107" opacity="0.07"/>
        <rect x="800" y="0" width="4" height="1107" opacity="0.12"/>
        <rect x="852" y="0" width="10" height="1107" opacity="0.08"/>
      </g>
    </svg>
    <div class="base-band"></div>
    <p class="author">Clive Mortlock</p>
    <h1 class="title">
      <span class="title-line title-line--lead">The</span>
      <span class="title-line">Ultimate Guide</span>
      <span class="title-line">To Internet Banking</span>
    </h1>
  </main>
</body>
</html>
```